Advertisement for back of sporting brochure

Company: Gridiron Ascent / gridascentpro.example
Business: Football skills development for offensive and defensive positions
Slogan: Learn to play the game on and off the field
Company colors: Royal Blue (reflex blue), White, Cool Gray 11 or Cool Gray 4, safety green can be used for some highlighting
Phone#: 555-274-8813

We require an 8.5" x 11" size flyer advertising the company.
The flyer will be displayed on the back of a sporting event program.
The objective of the flyer is to get viewers to contact Gridiron Ascent by either website or phone.

Must have items in the flyer are:
* Logo
* Slogan (see above)
* website (see above)
* Phone #
* photos
* Testimonials
* Word from the owner (see below)

“ In just 3 short years Gridiron Ascent clients have shown that skill development with the coaches at GA works! Over these past 3 years GA has had 24 players in the Continental Pigskin Circuit and 28 players go on to play at the collegiate level. We are making an impact on teams at every level including the 2013 High School State Championships with over 20 players participating in the state games. We have also worked with young players producing the MVP and Captains of the 2013 OKYA State champion. If you want to surround yourself with winners and raise your level of play while having fun and gaining confidence call us today!"

The CALL TO ACTION (CTA) is critical! The objective is for the viewer to call the phone number provided, now! The CTA should not fall into the same paragraph as information verbiage.

Target Market(s)

Elementary, Middle & High School players and parents

Industry/Entity Type

Advertising

Requirements
Must have
• CALL TO ACTION (CTA)
Readers must themselves, want to be part of the Gridiron Ascent family
OR
The parent must want their student athlete to become the best football player they can be
Should not have
• RED

```html
<!DOCTYPE html>
<html lang="en">
<head>
<meta charset="utf-8">
<title>Gridiron Ascent Flyer</title>
<link href="https://fonts.googleapis.com/css2?family=Alfa+Slab+One&family=Questrial&family=Roboto+Condensed:wght@400;700&family=Roboto:wght@300;400;500;700&family=Tinos&display=swap" rel="stylesheet">
<style>
  :root {
    --navy-deep: #050b26;
    --navy: #0a1a5e;
    --royal: #0d2a8c;
    --royal-bright: #1b46c9;
    --sky: #2f8fe6;
    --white: #ffffff;
    --gray-light: #d9dce2;
    --gray-cool: #c7ccd6;
    --gray-mid: #8c9099;
    --gray-dark: #53565a;
    --page-bg: #e6e8ec;
  }
  * { margin: 0; padding: 0; box-sizing: border-box; }
  html, body { width: 1200px; height: 857px; overflow: hidden; background: var(--page-bg); }
  .flyer {
    position: absolute; left: 322px; top: 68px; width: 558px; height: 722px;
    overflow: hidden;
    background: linear-gradient(180deg, var(--navy-deep) 0%, var(--navy) 14%, var(--royal) 45%, #0b2477 78%, var(--royal) 100%);
    box-shadow: 0 6px 18px rgba(0,0,0,.35);
    font-family: "Questrial", sans-serif;
    color: var(--white);
  }
  .swooshes { position: absolute; left: 0; top: 300px; width: 558px; height: 380px; }
  .team-photo {
    position: absolute; left: 0; top: 110px; width: 558px; height: 190px;
    background:
      linear-gradient(90deg, rgba(40,70,170,.75) 0%, rgba(40,70,170,.15) 30%, rgba(40,70,170,0) 60%, rgba(30,50,120,.35) 100%),
      linear-gradient(180deg, rgba(10,26,94,0) 0%, #3a4670 18%, #9a9ea8 40%, #c4c7cd 55%, #8a8e98 75%, #4a5488 100%);
  }
  .brand {
    position: absolute; left: 0; right: 0; top: 44px;
    display: flex; align-items: center; justify-content: center; gap: 12px;
  }
  .brand-dot { width: 22px; height: 22px; border-radius: 50%; background: var(--white); }
  .brand-name {
    font-family: "Roboto Condensed", sans-serif; font-weight: 700;
    font-size: 34px; letter-spacing: 1.5px; text-transform: uppercase; color: var(--white);
  }
  .slogan {
    position: absolute; left: 0; right: 0; top: 232px; text-align: center;
    font-family: "Alfa Slab One", serif; font-size: 26px; line-height: 25px;
    letter-spacing: 2.5px; text-transform: uppercase; color: var(--white); font-weight: 400;
    text-shadow: 0 0 3px #000, 1px 1px 0 #111, -1px -1px 0 #111, 1px -1px 0 #111, -1px 1px 0 #111, 2px 3px 4px rgba(0,0,0,.6);
  }
  .wave { position: absolute; left: 0; top: 276px; width: 558px; height: 40px; }
  .coach-photo {
    position: absolute; left: 22px; top: 314px; width: 154px; height: 154px;
    border-radius: 50%; border: 6px solid var(--white);
    background: linear-gradient(180deg, #e4e6ea 0%, #b9bcc3 38%, #6f737b 60%, #4f535b 100%);
    box-shadow: 0 12px 16px rgba(0,0,0,.5);
  }
  .section-title {
    position: absolute; left: 191px;
    font-family: "Alfa Slab One", serif; font-size: 12.5px; letter-spacing: 1px; font-weight: 400;
    text-transform: uppercase; color: var(--white);
    text-shadow: 1px 1px 0 #000;
  }
  .about-title { top: 340px; }
  .about-copy {
    position: absolute; left: 191px; top: 359px; width: 340px;
    font-size: 8.6px; line-height: 11.3px; text-align: justify; color: var(--white);
  }
  .testimonial-title { top: 474px; }
  .testimonial-quote {
    position: absolute; left: 191px; top: 491px; width: 332px;
    font-family: "Roboto", sans-serif; font-size: 7.9px; line-height: 11.5px; font-weight: 500;
  }
  .testimonial-name {
    position: absolute; left: 191px; top: 534px;
    font-family: "Roboto", sans-serif; font-size: 7.6px; color: var(--gray-cool);
  }
  .testimonial-role {
    position: absolute; left: 191px; top: 546px;
    font-family: "Roboto", sans-serif; font-size: 7.6px; font-weight: 700; font-style: italic;
  }
  .cta-band {
    position: absolute; left: 150px; top: 575px; width: 392px; height: 48px;
    background: linear-gradient(90deg, rgba(47,143,230,0) 0%, rgba(47,143,230,.45) 40%, rgba(27,70,201,.6) 100%);
  }
  .cta-text {
    position: absolute; right: 28px; top: 580px; width: 360px; text-align: right;
    font-family: "Roboto", sans-serif; font-size: 9.6px; line-height: 12px;
  }
  .cta-text strong { font-weight: 700; }
  .social {
    position: absolute; left: 42px; top: 628px; display: flex; align-items: center; gap: 4px;
    font-family: "Roboto", sans-serif; font-size: 16px;
  }
  .social-find { font-weight: 300; margin-right: 3px; }
  .social-us { font-weight: 700; margin-right: 3px; }
  .social-square { width: 18px; height: 18px; border-radius: 2px; background: var(--white); }
  .phone {
    position: absolute; right: 28px; top: 614px;
    font-family: "Roboto Condensed", sans-serif; font-weight: 700; font-size: 37px; letter-spacing: .5px;
  }
  .web-bar {
    position: absolute; left: 0; top: 669px; width: 558px; height: 26px;
    background: linear-gradient(180deg, #ffffff 0%, #e4e6ea 100%);
    text-align: center; line-height: 26px;
    font-family: "Tinos", serif; font-size: 11.5px; letter-spacing: 3.6px;
    color: var(--gray-dark);
  }
  .foot-band {
    position: absolute; left: 0; top: 695px; width: 558px; height: 27px;
    background: linear-gradient(180deg, var(--royal-bright) 0%, var(--royal) 100%);
  }
</style>
</head>
<body>
  <main class="flyer">
    <svg class="swooshes" viewBox="0 0 558 380" aria-hidden="true">
      <path d="M0 250 C 150 150, 350 120, 558 60" fill="none" stroke="#2f8fe6" stroke-opacity=".18" stroke-width="30"/>
      <path d="M0 300 C 180 210, 380 180, 558 140" fill="none" stroke="#2f8fe6" stroke-opacity=".14" stroke-width="18"/>
      <path d="M60 380 C 200 300, 400 280, 558 270" fill="none" stroke="#5aa8f0" stroke-opacity=".16" stroke-width="40"/>
    </svg>

    <div class="team-photo" role="img" aria-label="Black and white group photo of the team and coaches on an indoor field"></div>

    <div class="brand">
      <span class="brand-dot"></span>
      <span class="brand-name">Gridiron Ascent</span>
    </div>

    <h1 class="slogan">Learn to play the game<br>on and off the field</h1>

    <svg class="wave" viewBox="0 0 558 40" aria-hidden="true">
      <path d="M0 8 L278 24 L558 8 L558 40 L0 40 Z" fill="#0d2a8c"/>
      <path d="M0 8 L278 24 L558 8" fill="none" stroke="#ffffff" stroke-width="3"/>
    </svg>

    <div class="coach-photo" role="img" aria-label="Coach running an agility drill with a player over low hurdles"></div>

    <h2 class="section-title about-title">About Us</h2>
    <p class="about-copy">In just 3 short years Gridiron Ascent clients have shown that skill development with the coaches at GA works! Over these past 3 years GA has had 24 players in the Continental Pigskin Circuit and 28 players go on to play at the collegiate level. We are making an impact on teams at every level including the 2013 High School State Championships with over 20 players participating in the state games. We have also worked with young players producing the MVP and Captains of the 2013 OKYA State champion.</p>

    <h2 class="section-title testimonial-title">Testimonial</h2>
    <p class="testimonial-quote">I've known Marcus Holloway most of my nearly 20 year coaching career. In a profession where you stress character, honesty, loyalty, commitment and determination, it has been truly an honor...</p>
    <p class="testimonial-name">Warren Calloway</p>
    <p class="testimonial-role">Assistant Football Coach - Lakeshore Ridge University</p>

    <div class="cta-band"></div>
    <p class="cta-text">If you want to surround yourself with winners and raise your level of play<br>while having fun and gaining confidence<br><strong>call us today!</strong></p>

    <div class="social"><span class="social-find">FIND</span><span class="social-us">US</span><span class="social-square"></span><span class="social-square"></span></div>
    <p class="phone">555-274-8813</p>

    <div class="web-bar">www.gridascentpro.example</div>
    <div class="foot-band"></div>
  </main>
</body>
</html>
```